Latin CBD company needs a design for a counter display box

-We would like a design for a display box for our restorative CBD oil tinctures. We would like to stand out our brand promoting wellness being and health. However, because its targeting the latin market, we would like to see color on it.
- The display box is for CBD tinctures (image attached)
-I am attaching two files, if you are Spanish speaker it would be nice to see the design in Spanish. Thank you!
THANK YOU IN ADVANCE FOR WORKING IN OUR PROJECT!

Font styles to use
Serif
Sans Serif

```html
<!DOCTYPE html>
<html lang="es">
<head>
<meta charset="utf-8">
<title>Selva Viva CBD – Caja exhibidora</title>
<link rel="stylesheet" href="https://fonts.googleapis.com/css2?family=Oswald:wght@400;500&family=Poppins:wght@400;500&display=swap">
<style>
  :root{
    --bg:#66286f;
    --green:#5aad3c;
    --purple:#5f2470;
    --white:#ffffff;
    --rule:#9a9a9a;
    --ink:#3b1447;
  }
  html,body{margin:0;padding:0;width:1200px;height:1200px;overflow:hidden;background:var(--bg);}
  .dieline{display:block;width:1200px;height:1200px;}
  .panel{fill:var(--white);}
  .band{fill:var(--green);}
  .fold{stroke:var(--rule);stroke-width:1;fill:none;}
  .perf{stroke:#777;stroke-width:1;stroke-dasharray:5 4;fill:none;}
  .cut{stroke:#333;stroke-width:1;fill:none;}
  .brand{font-family:"Poppins",sans-serif;font-weight:400;}
  .cond{font-family:"Oswald",sans-serif;font-weight:400;}
  .brand-white{fill:var(--white);}
  .brand-green{fill:var(--green);}
  .txt-purple{fill:var(--purple);}
  .txt-ink{fill:var(--ink);}
  .txt-white{fill:var(--white);}
  .mark{fill:none;stroke:var(--white);stroke-width:2.5;}
  .mark-green{fill:none;stroke:var(--green);stroke-width:2.5;}
  .mark-purple{fill:none;stroke:var(--purple);stroke-width:2;}
  .ghost{fill:none;stroke:#cfcfcf;stroke-width:3;}
</style>
</head>
<body>
<svg class="dieline" viewBox="40 240 1420 1200" preserveAspectRatio="xMidYMid meet" xmlns="http://www.w3.org/2000/svg">

  <!-- Glue flap -->
  <polygon class="panel" points="123,815 62,925 62,1140 123,1228"/>

  <!-- Left side panel -->
  <g class="side-left">
    <polygon class="band" points="135,755 375,755 375,800 388,815 123,815 135,800"/>
    <rect class="panel" x="123" y="815" width="265" height="413"/>
    <rect class="band" x="123" y="815" width="265" height="98"/>
    <path class="band" d="M123,1175 L218,1175 L238,1198 L388,1198 L388,1228 L123,1228 Z"/>
    <line class="cut" x1="123" y1="815" x2="388" y2="1080"/>
    <circle class="ghost" cx="270" cy="1110" r="82"/>
    <circle class="mark-green" cx="210" cy="1018" r="22"/>
    <text class="brand brand-green" x="133" y="1063" font-size="22">SELVA VIVA CBD</text>
    <text class="brand brand-green" x="133" y="1089" font-size="16">Sabor natural</text>
    <g class="cond txt-ink" font-size="10.5">
      <text x="133" y="1110">• No psicoactivo</text>
      <text x="133" y="1125">• Espectro Completo</text>
      <text x="133" y="1140">• Fortalece el Sistema Endocananbinoide</text>
      <text x="133" y="1155">• 100% hecho de plantas naturales cultivadas en Colorado</text>
    </g>
    <text class="cond txt-white" x="131" y="1220" font-size="40" font-weight="500">6</text>
    <text class="cond txt-white" x="154" y="1199" font-size="18">Tincture</text>
    <text class="cond txt-white" x="154" y="1219" font-size="18">Bottles</text>
    <text class="cond txt-ink" x="256" y="1213" font-size="11">300 mg CBD • 1 Fl Oz (30ml)</text>
  </g>
  <polygon class="panel" points="123,1228 388,1228 388,1290 310,1360 310,1415 200,1415 200,1360 123,1275"/>

  <!-- Front panel -->
  <g class="front">
    <rect class="panel" x="388" y="815" width="392" height="413"/>
    <path class="band" d="M388,815 H780 V913 H735 L722,955 H453 L440,913 H388 Z"/>
    <circle class="mark" cx="584" cy="869" r="36"/>
    <text class="brand brand-white" x="584" y="937" font-size="31" text-anchor="middle">SELVA VIVA CBD</text>
    <text class="cond txt-purple" x="584" y="1000" font-size="24" font-weight="500" text-anchor="middle">Aceite Restaurador de CBD</text>
    <text class="cond txt-purple" x="584" y="1030" font-size="24" font-weight="500" text-anchor="middle">Hemp Oil Extract</text>
    <line class="perf" x1="388" y1="1131" x2="780" y2="1131"/>
    <circle class="mark-purple" cx="439" cy="1180" r="24"/>
    <text class="cond txt-purple" x="473" y="1177" font-size="12">DESCUBRE LOS BENEFICIOS DE VIVIR PLENAMENTE SALUDABLE</text>
    <text class="cond txt-purple" x="473" y="1193" font-size="12">ENJOY THE BENEFITS OF HEALTHY LIVING</text>
    <rect class="band" x="388" y="1220" width="392" height="8"/>
  </g>
  <polygon class="panel" points="388,1228 780,1228 640,1330 700,1415 388,1415"/>

  <!-- Right side panel -->
  <g class="side-right">
    <polygon class="band" points="793,755 1032,755 1032,800 1045,815 780,815 793,800"/>
    <rect class="panel" x="780" y="815" width="265" height="413"/>
    <rect class="band" x="780" y="815" width="265" height="98"/>
    <path class="band" d="M1045,1175 L950,1175 L930,1198 L780,1198 L780,1228 L1045,1228 Z"/>
    <line class="perf" x1="1045" y1="815" x2="780" y2="1125"/>
    <circle class="ghost" cx="898" cy="1110" r="82"/>
    <circle class="mark-green" cx="958" cy="1018" r="22"/>
    <text class="brand brand-green" x="1035" y="1063" font-size="22" text-anchor="end">SELVA VIVA CBD</text>
    <text class="brand brand-green" x="1035" y="1089" font-size="16" text-anchor="end">Sabor natural</text>
    <g class="cond txt-ink" font-size="10.5" text-anchor="end">
      <text x="1035" y="1110">No psicoactivo •</text>
      <text x="1035" y="1125">Espectro Completo •</text>
      <text x="1035" y="1140">Fortalece el Sistema Endocananbinoide •</text>
      <text x="1035" y="1155">100% hecho de plantas naturales cultivadas en Colorado •</text>
    </g>
    <text class="cond txt-white" x="956" y="1220" font-size="40" font-weight="500">6</text>
    <text class="cond txt-white" x="979" y="1199" font-size="18">Tincture</text>
    <text class="cond txt-white" x="979" y="1219" font-size="18">Bottles</text>
    <text class="cond txt-ink" x="790" y="1213" font-size="11">300 mg CBD • 1 Fl Oz (30ml)</text>
  </g>
  <polygon class="panel" points="780,1228 1045,1228 1045,1415 968,1415 968,1340 857,1340 857,1415 780,1415"/>

  <!-- Back + top panels -->
  <g class="back">
    <polygon class="panel" points="1065,258 1418,258 1437,548 1045,548"/>
    <rect class="panel" x="1045" y="548" width="392" height="680"/>
    <line class="fold" x1="1045" y1="548" x2="1437" y2="548"/>
    <line class="fold" x1="1045" y1="815" x2="1437" y2="815"/>
    <line class="fold" x1="1045" y1="1228" x2="1437" y2="1228"/>
    <line class="fold" x1="780" y1="1228" x2="1045" y2="1228"/>
    <line class="fold" x1="388" y1="1228" x2="780" y2="1228"/>
    <line class="fold" x1="123" y1="1228" x2="388" y2="1228"/>

    <rect class="band" x="1045" y="662" width="392" height="36"/>
    <path class="band" d="M1170,698 L1180,745 H1302 L1312,698 Z"/>

    <g class="top-half">
      <circle class="mark" cx="1241" cy="708" r="13"/>
      <text class="brand brand-white" x="1241" y="734" font-size="14" text-anchor="middle">SELVA VIVA CBD</text>
      <text class="cond txt-ink" x="1241" y="764" font-size="13" text-anchor="middle">Aceite Restaurador de CBD</text>
      <text class="cond txt-ink" x="1241" y="781" font-size="13" text-anchor="middle">Hemp Oil Extract</text>
      <text class="cond txt-purple" x="1060" y="750" font-size="38" font-weight="500">6</text>
      <text class="cond txt-purple" x="1083" y="730" font-size="18">Tincture</text>
      <text class="cond txt-purple" x="1083" y="750" font-size="18">Bottles</text>
      <text class="cond txt-ink" x="1421" y="727" font-size="16" text-anchor="end">300 mg CBD</text>
      <text class="cond txt-ink" x="1421" y="748" font-size="16" text-anchor="end">1 Fl Oz (30ml)</text>
    </g>
    <g class="top-half" transform="rotate(180 1241 680)">
      <path class="band" d="M1170,698 L1180,745 H1302 L1312,698 Z"/>
      <circle class="mark" cx="1241" cy="708" r="13"/>
      <text class="brand brand-white" x="1241" y="734" font-size="14" text-anchor="middle">SELVA VIVA CBD</text>
      <text class="cond txt-ink" x="1241" y="764" font-size="13" text-anchor="middle">Aceite Restaurador de CBD</text>
      <text class="cond txt-ink" x="1241" y="781" font-size="13" text-anchor="middle">Hemp Oil Extract</text>
      <text class="cond txt-purple" x="1060" y="750" font-size="38" font-weight="500">6</text>
      <text class="cond txt-purple" x="1083" y="730" font-size="18">Tincture</text>
      <text class="cond txt-purple" x="1083" y="750" font-size="18">Bottles</text>
      <text class="cond txt-ink" x="1421" y="727" font-size="16" text-anchor="end">300 mg CBD</text>
      <text class="cond txt-ink" x="1421" y="748" font-size="16" text-anchor="end">1 Fl Oz (30ml)</text>
    </g>

    <g class="cond txt-ink" font-size="13.5" text-anchor="middle">
      <text x="1241" y="897">Selva Viva CBD es la primer compañía de aceite de CBD dirigida</text>
      <text x="1241" y="917">principalmente a la comunidad latina en los Estados Unidos. Nace</text>
      <text x="1241" y="936">en el año 2017 ante la necesidad de dar a conocer los beneficios y</text>
      <text x="1241" y="956">usos de ésta planta milenaria y terapéutica, que ofrece beneficios</text>
      <text x="1241" y="975">extraordinarios para nuestra salud de forma 100% natural, y sin</text>
      <text x="1241" y="995">ningún efecto psicoactivo o secundario.</text>
      <text x="1241" y="1039">En Selva Viva CBD nos sentimos orgullosos de poder brindar la más alta</text>
      <text x="1241" y="1058">calidad de productos de CBD provenientes de cultivos de plantas</text>
      <text x="1241" y="1078">orgánicas de Cáñamo en el estado de Colorado, el cual es conocido</text>
      <text x="1241" y="1097">por sus espectaculares escenarios naturales que incluyen ríos,</text>
      <text x="1241" y="1117">montañas, mesetas y diferentes ecosistemas naturales. Un lugar</text>
      <text x="1241" y="1136">que nos ofrece las bondades de sus suelos y altitud perfecta para</text>
      <text x="1241" y="1156">crecer ésta variedad de planta terapéutica y medicinal</text>
    </g>
  </g>
  <polygon class="panel" points="1045,1228 1437,1228 1437,1415 1125,1415 1195,1335"/>
</svg>
</body>
</html>
```